Fast Business Card Project

I need a business card with the name RENATO COSTA stylized on one side and my email on the other (renatolima4711@mailbrisa.com)

Industry/Entity Type

Business

Contact Information for Business Card

www.trilvento.com.br

```html
<!DOCTYPE html>
<html lang="en">
<head>
<meta charset="utf-8">
<title>Renato Costa — Business Card</title>
<link rel="stylesheet" href="https://fonts.googleapis.com/css2?family=Questrial&family=Roboto:wght@400&display=swap">
<style>
  :root {
    --page-bg: #e9e7e4;
    --card-light: #ffffff;
    --card-mid: #eeeeee;
    --card-shade: #d9d9d9;
    --ink: #1c1c1c;
    --icon-dark: #2b2b2b;
    --accent-red: #e0262b;
    --on-accent: #ffffff;
  }
  * { margin: 0; padding: 0; box-sizing: border-box; }
  html, body {
    width: 1200px;
    height: 800px;
    overflow: hidden;
    background: var(--page-bg);
  }
  .sheet {
    width: 1200px;
    height: 800px;
    display: flex;
    align-items: center;
    justify-content: center;
    gap: 40px;
  }
  .card {
    position: relative;
    width: 540px;
    height: 310px;
    overflow: hidden;
    box-shadow: 0 6px 18px rgba(0, 0, 0, 0.18);
  }
  .card-backdrop {
    position: absolute;
    inset: 0;
    background:
      radial-gradient(ellipse at 70% 35%, var(--card-light) 0%, var(--card-mid) 55%, var(--card-shade) 100%);
  }
  .brand {
    position: absolute;
    display: flex;
    align-items: center;
    gap: 16px;
  }
  .brand-square {
    width: 30px;
    height: 30px;
    background: var(--ink);
  }
  .brand-name {
    font-family: "Questrial", "Century Gothic", sans-serif;
    font-size: 36px;
    letter-spacing: 0.5px;
    color: var(--ink);
    line-height: 1;
  }
  .card--front .brand { left: 96px; top: 136px; }
  .card--back .brand { left: 40px; top: 88px; }
  .contact {
    position: absolute;
    left: 40px;
    top: 190px;
  }
  .contact-icon {
    width: 52px;
    height: 52px;
    border-radius: 50%;
    background: var(--icon-dark);
    display: flex;
    align-items: center;
    justify-content: center;
    margin-left: 4px;
  }
  .contact-email {
    margin-top: 10px;
    display: inline-block;
    background: var(--accent-red);
    color: var(--on-accent);
    font-family: "Roboto", Arial, sans-serif;
    font-size: 14px;
    line-height: 1;
    padding: 5px 12px 6px;
    border-radius: 6px;
  }
</style>
</head>
<body>
  <main class="sheet">
    <section class="card card--front">
      <div class="card-backdrop" role="img" aria-label="Soft white photograph of piled white spheres"></div>
      <div class="brand">
        <span class="brand-square"></span>
        <span class="brand-name">RENATO COSTA</span>
      </div>
    </section>

    <section class="card card--back">
      <div class="card-backdrop" role="img" aria-label="Soft white photograph of piled white spheres"></div>
      <div class="brand">
        <span class="brand-square"></span>
        <span class="brand-name">RENATO COSTA</span>
      </div>
      <div class="contact">
        <div class="contact-icon">
          <svg width="26" height="18" viewBox="0 0 26 18" aria-hidden="true">
            <rect x="1" y="1" width="24" height="16" fill="#ffffff" stroke="#ffffff" stroke-width="1"/>
            <polyline points="1,1 13,10 25,1" fill="none" stroke="#2b2b2b" stroke-width="1.6"/>
            <line x1="1" y1="17" x2="10" y2="8" stroke="#2b2b2b" stroke-width="1.2"/>
            <line x1="25" y1="17" x2="16" y2="8" stroke="#2b2b2b" stroke-width="1.2"/>
          </svg>
        </div>
        <span class="contact-email">renatolima4711@mailbrisa.com</span>
      </div>
    </section>
  </main>
</body>
</html>
```